New LGBT Nightclub Crowdfunding Poster

We need it to read well for social media posts. All colors should look similar to Seattle’s Sports Teams color schemes.

The top should have: The logo prominently with the fans in the background photo. and then still center and important, "Coming soon!" "You can be part of the first in line for the amazing things happening". (The call to action is the purchase of these amazing deals for the first weekend open / passes. That should be clear).

```html
<!DOCTYPE html>
<html lang="en">
<head>
<meta charset="utf-8">
<title>The Encore – Coming Soon Poster</title>
<link rel="stylesheet" href="https://fonts.googleapis.com/css2?family=Righteous&family=Questrial&family=Carlito:ital,wght@0,400;0,700;1,400;1,700&display=swap">
<style>
  :root{
    --navy:#0c1446;
    --blue:#3b6fd6;
    --lime:#c8cc2c;
    --lime-bright:#e4ec3c;
    --gold:#c9b43b;
    --white:#ffffff;
    --ink:#1b1b2a;
    --stage:#e6e7ec;
  }
  *{margin:0;padding:0;box-sizing:border-box}
  html,body{width:1200px;height:1200px;overflow:hidden;background:var(--stage)}
  .poster{position:absolute;left:176px;top:70px;width:848px;height:1060px;background:var(--white);overflow:hidden}
  .poster-shapes{position:absolute;inset:0}
  .logo{position:absolute;left:-6px;top:4px;width:272px;height:272px;border-radius:50%;
    background:var(--white);border:6px solid var(--lime);display:flex;flex-direction:column;
    align-items:center;justify-content:center;gap:6px}
  .logo-name{font-family:"Righteous",sans-serif;font-size:34px;color:var(--navy);letter-spacing:1px;line-height:1;text-align:center}
  .logo-dot{width:14px;height:14px;border-radius:50%;background:var(--navy)}
  .headline{position:absolute;left:336px;top:350px;width:480px;transform:rotate(-8deg);transform-origin:left top}
  .headline-title{font-family:"Righteous",sans-serif;font-size:60px;color:var(--white);
    -webkit-text-stroke:2px var(--navy);line-height:1;white-space:nowrap}
  .headline-title .accent{color:var(--lime-bright)}
  .headline-sub{font-family:"Questrial",sans-serif;font-size:31px;color:var(--white);line-height:1.05;
    text-align:center;margin-top:4px;white-space:nowrap}
  .headline-sub strong{color:var(--lime-bright);font-weight:400;font-family:"Righteous",sans-serif}
  .cta{position:absolute;left:0;top:0;width:322px;height:1060px;text-align:center;color:var(--white)}
  .cta p{position:absolute;left:0;width:100%}
  .cta-buy{top:594px;font-family:"Righteous",sans-serif;font-size:62px;color:var(--gold);line-height:1}
  .cta-these{top:666px;font-family:"Righteous",sans-serif;font-size:31px;line-height:1}
  .cta-deals{top:708px;font-family:"Righteous",sans-serif;font-size:27px;line-height:1}
  .cta-note{top:836px;font-family:"Questrial",sans-serif;font-size:25px;line-height:1.25}
  .offers{position:absolute;right:0;top:548px;width:520px;list-style:none}
  .offer{position:absolute;right:0;width:520px;display:flex;align-items:center;justify-content:flex-end;gap:10px}
  .offer-text{font-family:"Carlito",sans-serif;font-size:16px;line-height:1.3;color:var(--ink);text-align:right}
  .offer-text b{font-weight:700}
  .offer-text em{font-style:italic;font-weight:700}
  .offer-text .hl{color:var(--blue)}
  .offer-price{flex:none;width:78px;height:40px;display:flex;align-items:center;justify-content:center;
    font-family:"Righteous",sans-serif;font-size:17px}
  .price-lime{background:var(--lime);color:var(--navy)}
  .price-blue{background:var(--blue);color:var(--white)}
  .price-navy{background:var(--navy);color:var(--white)}
  .footer-note{position:absolute;left:32px;top:1002px;font-family:"Carlito",sans-serif;font-size:17px;color:var(--white);line-height:1.3}
  .phone{position:absolute;right:28px;top:1010px;display:flex;align-items:center;gap:10px;
    font-family:"Righteous",sans-serif;font-size:34px;color:var(--navy)}
</style>
</head>
<body>
<main class="poster">
  <svg class="poster-shapes" width="848" height="1060" viewBox="0 0 848 1060">
    <defs>
      <radialGradient id="crowdBlue" cx="0.5" cy="0.6" r="0.8">
        <stop offset="0" stop-color="#2c3ad0"/><stop offset="1" stop-color="#0a1260"/>
      </radialGradient>
      <radialGradient id="crowdLime" cx="0.6" cy="0.2" r="0.9">
        <stop offset="0" stop-color="#e9ef5a"/><stop offset="0.6" stop-color="#8c8f1e"/><stop offset="1" stop-color="#2a2c10"/>
      </radialGradient>
    </defs>
    <rect x="380" y="0" width="468" height="20" fill="var(--blue)"/>
    <polygon class="photo-crowd" role="img" aria-label="Photo of a concert crowd with raised hands, tinted blue" points="0,0 500,0 500,460 0,460" fill="url(#crowdBlue)"/>
    <polygon class="photo-stage" role="img" aria-label="Photo of fans making a heart with their hands under stage lights, tinted yellow-green" points="455,18 848,18 848,380 380,460" fill="url(#crowdLime)"/>
    <polygon points="0,328 156,400 0,458" fill="var(--gold)"/>
    <polygon points="0,440 848,330 848,460 0,528" fill="var(--blue)"/>
    <polygon points="0,472 360,456 288,966 0,966" fill="var(--navy)"/>
    <line x1="551" y1="522" x2="848" y2="494" stroke="var(--lime)" stroke-width="5"/>
    <g class="cta-burst" stroke-width="4" stroke-linecap="round">
      <line x1="92" y1="522" x2="106" y2="566" stroke="var(--lime)"/>
      <line x1="161" y1="516" x2="161" y2="568" stroke="var(--white)"/>
      <line x1="230" y1="522" x2="216" y2="566" stroke="var(--blue)"/>
      <line x1="106" y1="760" x2="92" y2="804" stroke="var(--blue)"/>
      <line x1="161" y1="756" x2="161" y2="808" stroke="var(--white)"/>
      <line x1="216" y1="760" x2="230" y2="804" stroke="var(--lime)"/>
    </g>
    <polygon points="0,968 400,1012 340,1060 0,1060" fill="var(--blue)"/>
    <polygon points="290,1060 848,958 848,1060" fill="var(--lime)"/>
  </svg>

  <div class="logo">
    <span class="logo-name">THE<br>ENCORE</span>
    <span class="logo-dot"></span>
  </div>

  <header class="headline">
    <h1 class="headline-title">COMING <span class="accent">SOON!</span></h1>
    <p class="headline-sub">You can be part of the<br>first in line for the <strong>AMAZING</strong><br>things happening!</p>
  </header>

  <section class="cta">
    <p class="cta-buy">BUY</p>
    <p class="cta-these">THESE</p>
    <p class="cta-deals">AMAZING DEALS</p>
    <p class="cta-note">for the first<br>weekend open<br>/ passes.</p>
  </section>

  <ul class="offers">
    <li class="offer" style="top:8px">
      <span class="offer-text">Opening FRI/SAT night <b>Glitter GA Ticket with<br>Drag Megastar</b>. (<em>Only <span class="hl">100</span> available /night</em>)</span>
      <span class="offer-price price-lime">$25</span></li>
    <li class="offer" style="top:66px">
      <span class="offer-text">Opening FRI/SAT night <b>Glitter Third Tier Seating</b><br>(<em>Only <span class="hl">60</span> available /night</em>)</span>
      <span class="offer-price price-blue">$50</span></li>
    <li class="offer" style="top:124px">
      <span class="offer-text">Opening FRI/SAT night Glitter Middle Tier Seating<br>w/secret Drag Megastar (<em>Only <span class="hl">60</span> available /night</em>)</span>
      <span class="offer-price price-navy">$75</span></li>
    <li class="offer" style="top:184px">
      <span class="offer-text">Opening FRI/SAT night Glitter VIP Ticket with<br>Secret Drag Megastar (<em>Only <span class="hl">60</span> available /night</em>)</span>
      <span class="offer-price price-lime">$100</span></li>
    <li class="offer" style="top:236px">
      <span class="offer-text"><b>THE ENCORE PASS</b> Skip the line &amp; <b class="hl">FREE</b> cover for<br>6 months. Not including Brunch Shows &amp; Special<br>Events. Plus The Encore Merch. (<em><span class="hl">50</span> Available</em>)</span>
      <span class="offer-price price-blue">$500</span></li>
    <li class="offer" style="top:320px">
      <span class="offer-text"><b>THE ENCORE GOLD PASS</b> Skip the line &amp; <b class="hl">FREE</b> cover<br>for the year. Not including Brunch Shows &amp; Special Events.<br>Plus The Encore Merch. (<em><span class="hl">100</span> Available</em>)</span>
      <span class="offer-price price-navy">$1,000</span></li>
  </ul>

  <p class="footer-note">Ask about the<br>Encore Elite Pass</p>

  <div class="phone">
    <svg width="34" height="34" viewBox="0 0 34 34" aria-hidden="true">
      <circle cx="17" cy="17" r="17" fill="var(--blue)"/>
      <path d="M12 9c1 0 2 2.5 2.5 3.5.4.8-.6 1.6-1 2.2.8 1.8 2.3 3.3 4 4.2.6-.4 1.4-1.5 2.2-1 1 .5 3.4 1.6 3.3 2.6-.2 1.6-1.6 3-3.3 2.8C14 22.6 9.5 18 9 12.4 8.8 10.6 10.4 9 12 9z" fill="var(--white)"/>
    </svg>
    <span>206 555 0148</span>
  </div>
</main>
</body>
</html>
```